Custom Apparel Decorating Company needs a Website Home Page Banner Design

We are in need of a website Home page banner design for a small company based in Canada called Quellmont. We are a custom apparel company that offers custom apparel (t-shirts, hoodies, hats etc) to Companies, Organizations/groups, bands, Spirit wear and individuals. We would like the design to match with the logo files we have attached to the campaign. The Website has not been created yet planning to tie the website into the home page banner for flow. Thinking of using Duda or Shopify for the website if that helps! We are really looking forward to seeing the designs.

Target Market(s)

Companies, Organizations/Groups, Bands, Spirit wear and Individuals. Anyone that is looking to have there company or own logo/Design put on a piece of clothing.

Requirements
Must have
• -Colours in the logo files.
• -FUN creating the Home Page Banner!!! :)
Nice to have
• -Up Beat feel to it (it's the first image you will see when you go to the website, it's the store front so we want to grab the attention of the potential customers)

```html
<!DOCTYPE html>
<html lang="en">
<head>
<meta charset="UTF-8">
<title>Quellmont Apparel – Home Banner</title>
<link href="https://fonts.googleapis.com/css2?family=Raleway:wght@300;400;700&display=swap" rel="stylesheet">
<style>
  :root {
    --page-bg: #e4e4e4;
    --banner-bg: #f4f4f4;
    --brand-blue: #4670b9;
    --ink: #1c1c1c;
    --body-text: #333333;
    --white: #ffffff;
    --wall-dark: #2b2a28;
    --sweater: #cfc8b0;
    --denim: #1f2a44;
  }
  * { margin: 0; padding: 0; box-sizing: border-box; }
  html, body { width: 1200px; height: 1200px; overflow: hidden; }
  body {
    background: var(--page-bg);
    font-family: "Raleway", sans-serif;
    position: relative;
  }
  .banner {
    position: absolute;
    left: 0; top: 150px;
    width: 1200px; height: 900px;
    background: var(--banner-bg);
    overflow: hidden;
  }
  .corner-flag { position: absolute; left: 0; top: 0; }

  .collage { position: absolute; left: 0; top: 0; width: 640px; height: 900px; }
  .collage-tile {
    position: absolute;
    border: 3px solid var(--white);
  }
  .tile-a { left: 108px; top: 117px; width: 242px; height: 250px;
    background: linear-gradient(160deg, var(--wall-dark) 0%, #5a5246 55%, var(--sweater) 100%); }
  .tile-b { left: 372px; top: 48px; width: 250px; height: 240px; transform: rotate(12deg);
    background: linear-gradient(200deg, #1e1d1b 0%, #3c3933 60%, #8b8170 100%); }
  .tile-c { left: 308px; top: 279px; width: 262px; height: 229px;
    background: linear-gradient(180deg, #b9b29c 0%, var(--sweater) 50%, #7d7766 100%); }
  .tile-d { left: 312px; top: 508px; width: 258px; height: 258px;
    background: linear-gradient(180deg, var(--sweater) 0%, #8f8875 45%, var(--denim) 100%); }
  .tile-e { left: 67px; top: 378px; width: 242px; height: 200px; transform: rotate(-8deg);
    background: linear-gradient(150deg, var(--wall-dark) 0%, #8b8572 50%, var(--sweater) 100%); }
  .tile-f { left: 46px; top: 575px; width: 258px; height: 258px;
    background: linear-gradient(200deg, #c5bea8 0%, #4a4138 50%, #2a2622 100%); }

  .brand {
    position: absolute; left: 712px; top: 88px; width: 400px;
    display: flex; align-items: center; justify-content: center; gap: 14px;
  }
  .brand-mark { width: 34px; height: 34px; background: var(--brand-blue); }
  .brand-name {
    font-weight: 700; font-size: 34px; letter-spacing: 2px;
    color: var(--brand-blue); text-transform: uppercase;
  }

  .headline-blob { position: absolute; left: 575px; top: 212px; }
  .headline {
    position: absolute; left: 660px; top: 248px; width: 500px;
    text-align: center; font-weight: 700; font-size: 80px; line-height: 104px;
  }
  .headline .blue { color: var(--brand-blue); display: block; }
  .headline .white { color: var(--white); display: block; }

  .tagline {
    position: absolute; left: 660px; top: 670px; width: 500px;
    text-align: center; font-weight: 400; font-size: 26px; line-height: 38px;
    color: var(--body-text);
  }
  .shop-button {
    position: absolute; left: 812px; top: 779px; width: 196px; height: 60px;
    border-radius: 30px; background: var(--brand-blue); color: var(--white);
    font-size: 24px; font-weight: 400;
    display: flex; align-items: center; justify-content: center;
  }
</style>
</head>
<body>
  <section class="banner">
    <svg class="corner-flag" width="40" height="67" viewBox="0 0 40 67">
      <polygon points="0,0 40,33 0,67" fill="var(--brand-blue)"/>
    </svg>

    <div class="collage" role="img" aria-label="Photo collage of a bearded man in a cream sweater with navy stripes, seated against a dark wooden wall">
      <div class="collage-tile tile-b"></div>
      <div class="collage-tile tile-a"></div>
      <div class="collage-tile tile-e"></div>
      <div class="collage-tile tile-c"></div>
      <div class="collage-tile tile-d"></div>
      <div class="collage-tile tile-f"></div>
    </div>

    <div class="brand">
      <span class="brand-mark"></span>
      <span class="brand-name">Quellmont Apparel</span>
    </div>

    <svg class="headline-blob" width="625" height="421" viewBox="0 0 625 421">
      <path fill="var(--ink)" d="M112,38 C180,16 300,8 420,6 C500,4 560,2 600,10 C620,30 612,70 625,95 L625,300 C600,320 570,330 540,336 C480,350 400,356 330,358 C280,380 250,410 240,421 C230,390 215,365 190,360 C150,362 100,360 60,350 C40,340 45,320 60,300 C30,290 10,270 0,250 L0,150 C8,120 30,110 55,108 C80,100 100,92 110,80 C100,60 100,48 112,38 Z"/>
    </svg>

    <h1 class="headline">
      <span class="blue">T-shirts,</span>
      <span class="white">Hoodies,</span>
      <span class="blue">hats etc</span>
    </h1>

    <p class="tagline">We are a custom apparel company<br>that offers custom apparel</p>

    <div class="shop-button">Shop Now</div>
  </section>
</body>
</html>
```